Business card for Industrial Automation Company.

The company is called Process and Motion Solutions. We are a systems integration company in South Africa specializing in PLC and SCADA programming, systems integration and industrial automation. Attached find logo and cover letter of the company for a feel of the general look. The website is still under development, so you will have to use your own ideas.

Please blend the colors on the business card as per the logo colors. Must be clean, professional look. Please submit a creative professional design. If a background color is used please do not use dark colored backgrounds.

Target Market(s)

Mining

Industry/Entity Type

Engineering Consultant

Contact Information for Business Card

Fanie du Plessis (NDip Electrical LC; BSc)
Director / Systems Engineer

Postal Address
PO Box 2836
Karoostad
7451

Physical Address:
Bloubos Street 27
Karoostad
7451

Tel: +22 548 6172
Cell: +27 82 395 4820
Mail: faniep@pms-za.example
Web: www.pms-za.example

Font styles to use
Sans Serif

Colors

Designer to choose colors to be used in the design.

Requirements
Must have
• Backside of the card must also contain the following:
• Services
• *Industrial Automation
• *Control System design and configuration
• *Systems Integration
• *Equipment Supply
• Industries
• *Mining
• *Factory
• *Oil and Gas
Nice to have
• Colors must blend in with colors of logo. Not too much color and no dark backgrounds.
Should not have
• dark / black background. Preferably white / light background if any.

```html
<!DOCTYPE html>
<html lang="en">
<head>
<meta charset="utf-8">
<title>Process and Motion Solutions – Business Card</title>
<link rel="stylesheet" href="https://fonts.googleapis.com/css2?family=Roboto:wght@400;500&display=swap">
<style>
  :root{
    --bg:#e8e8e8;
    --paper:#ffffff;
    --paper-tint:#f3f3f3;
    --blue:#1f4b8e;
    --grey:#6d6e71;
    --ink:#333436;
    --rule:#b9b9b9;
    --dark:#4a4a4a;
    --accent:#c8d400;
  }
  *{box-sizing:border-box;margin:0;padding:0}
  html,body{width:1200px;height:726px;overflow:hidden}
  body{background:var(--bg);font-family:"Roboto",sans-serif;position:relative}

  .card{position:absolute;top:208px;width:540px;height:310px;background:var(--paper);
        box-shadow:0 2px 8px rgba(0,0,0,.12);overflow:hidden}
  .card--back{left:40px}
  .card--front{left:620px;background:linear-gradient(120deg,var(--paper) 45%,var(--paper-tint))}

  /* wordmark: company name in one colour and weight, with a plain circle */
  .brand{display:flex;align-items:center;color:var(--blue);font-weight:500;line-height:1;white-space:nowrap}
  .brand__dot{border-radius:50%;background:var(--blue);flex:none}

  /* back */
  .back__brand{position:absolute;left:0;right:0;top:48px;justify-content:center;font-size:30px}
  .back__brand .brand__dot{width:22px;height:22px;margin-right:12px}
  .back__tagline{position:absolute;left:0;right:0;top:100px;text-align:center;
        color:var(--grey);font-size:12px;letter-spacing:2.4px}
  .services{position:absolute;left:0;right:0;top:138px;text-align:center;
        color:var(--ink);font-size:14px;line-height:21px}
  .services .dot{display:inline-block;width:8px;height:8px;border-radius:50%;
        background:var(--blue);margin:0 6px;vertical-align:1px}
  .back__rule{position:absolute;left:0;right:0;top:236px;height:3px;background:var(--rule)}
  .back__band{position:absolute;left:0;right:0;top:244px;height:30px;background:var(--blue);
        color:#fff;font-size:14px;text-align:center;line-height:30px;letter-spacing:.5px}

  /* front */
  .front__brand{position:absolute;right:30px;top:66px;font-size:20px}
  .front__brand .brand__dot{width:16px;height:16px;margin-right:9px}
  .person{position:absolute;left:30px;top:110px}
  .person__name{color:var(--blue);font-size:22px;font-weight:500}
  .person__creds{color:var(--blue);font-size:14px;margin-top:2px}
  .person__title{color:var(--ink);font-size:12px;margin-top:8px;letter-spacing:.3px}

  .contact{position:absolute;list-style:none;font-size:13px;color:var(--ink)}
  .contact li{display:flex;align-items:center;height:17px;white-space:nowrap}
  .contact svg{width:12px;height:12px;margin-right:12px;fill:var(--blue);flex:none}
  .contact--direct{left:30px;top:212px}
  .contact--address{left:300px;top:156px}
  .contact--address li{height:19px}

  .front__strip{position:absolute;left:0;bottom:0;width:290px;height:12px;background:var(--dark)}
  .front__tab{position:absolute;right:0;bottom:0;width:250px;height:72px;background:var(--blue);
        border-top-left-radius:26px;color:#fff;font-size:11px;letter-spacing:.8px;
        display:flex;align-items:center;justify-content:center;padding:0 12px 0 16px;white-space:nowrap}
  .front__tab::before{content:"";position:absolute;left:0;bottom:0;width:4px;height:22px;background:var(--accent)}
</style>
</head>
<body>

<section class="card card--back">
  <div class="brand back__brand">
    <span class="brand__dot"></span>
    <span class="brand__name">Process and Motion Solutions</span>
  </div>
  <p class="back__tagline">Precision control for moving industry!</p>
  <p class="services">
    Industrial Automation<span class="dot"></span>Control System Design<br>
    and Configuration<span class="dot"></span>Systems Integration<span class="dot"></span>Equipment Supply<br>
    Industries<span class="dot"></span>Mining<span class="dot"></span>Factory<span class="dot"></span>Oil and Gas
  </p>
  <div class="back__rule"></div>
  <div class="back__band">www.pms-za.example</div>
</section>

<section class="card card--front">
  <div class="brand front__brand">
    <span class="brand__dot"></span>
    <span class="brand__name">Process and Motion Solutions</span>
  </div>

  <div class="person">
    <p class="person__name">Fanie du Plessis</p>
    <p class="person__creds">(NDip Electrical LC; BSc)</p>
    <p class="person__title">Director / Systems Engineer</p>
  </div>

  <ul class="contact contact--address">
    <li><svg viewBox="0 0 12 12" aria-hidden="true"><rect x="1" y="3" width="10" height="6" rx="1"/><rect x="6" y="9" width="1.5" height="3"/></svg>PO Box 2836 Karoostad 7451</li>
    <li><svg viewBox="0 0 12 12" aria-hidden="true"><path d="M6 0a4 4 0 0 0-4 4c0 3 4 8 4 8s4-5 4-8a4 4 0 0 0-4-4zm0 5.6A1.6 1.6 0 1 1 6 2.4a1.6 1.6 0 0 1 0 3.2z"/></svg>Bloubos Street 27 Karoostad 7451</li>
  </ul>

  <ul class="contact contact--direct">
    <li><svg viewBox="0 0 12 12" aria-hidden="true"><path d="M6 0a6 6 0 1 0 0 12A6 6 0 0 0 6 0zm0 1.2a4.8 4.8 0 1 1 0 9.6 4.8 4.8 0 0 1 0-9.6zM4 3.2l1 1.6-.6.8c.4.9 1.1 1.6 2 2l.8-.6 1.6 1-.6 1C6 9 3 6 3.2 3.8z"/></svg>+22 548 6172</li>
    <li><svg viewBox="0 0 12 12" aria-hidden="true"><path d="M1 4c0-2 2-3 5-3s5 1 5 3v1H8.5V3.8h-5V5H1zm2 2h6l2 5H1z"/></svg>+27 82 395 4820</li>
    <li><svg viewBox="0 0 12 12" aria-hidden="true"><path d="M0 2h12v8H0zm1.3 1.2V4l4.7 3 4.7-3v-.8L6 6.2z"/></svg>faniep@pms-za.example</li>
    <li><svg viewBox="0 0 12 12" aria-hidden="true"><circle cx="6" cy="6" r="5.4" fill="none" stroke="#1f4b8e" stroke-width="1.2"/><ellipse cx="6" cy="6" rx="2.2" ry="5.4" fill="none" stroke="#1f4b8e" stroke-width="1"/><rect x="0.6" y="5.5" width="10.8" height="1"/></svg>www.pms-za.example</li>
  </ul>

  <div class="front__strip"></div>
  <div class="front__tab">Precision control for moving industry!</div>
</section>

</body>
</html>
```